Business Card Design Project

Business card design based on the existing logo.
Updates

Target Market(s)

Small to medium business owners and CIO's looking for professional IT services.

Industry/Entity Type

Business

Font styles to use
Serif
Sans Serif

Requirements
Must have
• Logo, company name, company details

Text to appear on the business card
Name / Title:
Tom Whitlock
CEO

Address:
Veltra Limited
Level 1, 482 Korau Rd
P O Box 362
Ohakune 5918

Other details:
tom@veltra.co
Ph: 0800 519 306
Mob: +64 21 948 213
www.veltra.co

Nice to have
• I would look at both single and double sided options. My initial thought is double sided with just the logo with the grey framing for the front and the name and details on the back. But I'm open to other design options.

```html
<!DOCTYPE html>
<html lang="en">
<head>
<meta charset="utf-8">
<title>Veltra IT Solutions – Business Card</title>
<link rel="stylesheet" href="https://fonts.googleapis.com/css2?family=Ubuntu:wght@300;400;500&display=swap">
<style>
  :root {
    --page: #ffffff;
    --frame: #2a2a2a;
    --panel-white: #ffffff;
    --panel-grey: #646564;
    --tile-red: #c82233;
    --tile-orange: #f2763a;
    --tile-blue: #236db5;
    --tile-green: #6fc387;
    --brand: #1e5f86;
    --ink-light: #ffffff;
  }
  * { margin: 0; padding: 0; box-sizing: border-box; }
  html, body {
    width: 1200px; height: 923px; overflow: hidden;
    background: var(--page);
    font-family: "Ubuntu", sans-serif;
  }
  .canvas { position: relative; width: 1200px; height: 923px; }

  .card-side {
    position: absolute; top: 29px; width: 536px; height: 857px;
    background: var(--frame);
  }
  .card-front { left: 49px; }
  .card-back { left: 613px; }

  .panel { position: absolute; }
  .logo-panel {
    background: var(--panel-white);
    display: flex; align-items: center; justify-content: center; gap: 16px;
  }
  .card-front .logo-panel { left: 29px; top: 27px; width: 479px; height: 389px; }
  .card-back .logo-panel { left: 29px; top: 672px; width: 473px; height: 148px; }

  .brand-mark { border-radius: 50%; background: var(--brand); flex: none; }
  .card-front .brand-mark { width: 54px; height: 54px; }
  .card-back .brand-mark { width: 40px; height: 40px; }
  .brand-name { color: var(--brand); font-weight: 500; white-space: nowrap; letter-spacing: 0.5px; }
  .card-front .brand-name { font-size: 40px; }
  .card-back .brand-name { font-size: 32px; }

  .name-panel {
    left: 29px; top: 438px; width: 479px; height: 390px;
    background: var(--panel-grey); color: var(--ink-light);
    text-align: center; padding-top: 170px;
  }
  .person-name { font-size: 52px; font-weight: 500; line-height: 1; }
  .person-title { font-size: 29px; font-weight: 300; margin-top: 6px; letter-spacing: 1px; }

  .tile {
    position: absolute; width: 230px; height: 229px;
    color: var(--ink-light); text-align: center;
    font-size: 20px; font-weight: 400; line-height: 27px;
  }
  .tile svg { display: block; margin: 0 auto; }
  .tile-address { left: 29px; top: 96px; background: var(--tile-red); padding-top: 26px; }
  .tile-phone { left: 275px; top: 96px; background: var(--tile-orange); padding-top: 27px; }
  .tile-email { left: 29px; top: 343px; background: var(--tile-blue); padding-top: 60px; }
  .tile-web { left: 275px; top: 343px; background: var(--tile-green); padding-top: 53px; }
  .tile-address .tile-text { margin-top: 18px; }
  .tile-phone .tile-text { margin-top: 20px; }
  .tile-email .tile-text { margin-top: 26px; }
  .tile-web .tile-text { margin-top: 27px; }
</style>
</head>
<body>
<main class="canvas">
  <section class="card-side card-front">
    <div class="panel logo-panel">
      <span class="brand-mark"></span>
      <span class="brand-name">Veltra IT Solutions</span>
    </div>
    <div class="panel name-panel">
      <p class="person-name">Tom Whitlock</p>
      <p class="person-title">C.E.O</p>
    </div>
  </section>

  <section class="card-side card-back">
    <div class="tile tile-address">
      <svg width="34" height="48" viewBox="0 0 34 48" aria-hidden="true">
        <path d="M17 2C8.7 2 2 8.7 2 17c0 10 15 29 15 29s15-19 15-29C32 8.7 25.3 2 17 2z" fill="#fff"/>
        <circle cx="17" cy="17" r="8" fill="var(--tile-red)"/>
      </svg>
      <p class="tile-text">Veltra Limited<br>Level 1, 482 Korau Rd<br>P O Box 362,<br>Ohakune 5918</p>
    </div>
    <div class="tile tile-phone">
      <svg width="44" height="44" viewBox="0 0 44 44" aria-hidden="true">
        <rect width="44" height="44" rx="8" fill="#fff"/>
        <path d="M16 10c-3 1-5 3-4 7 2 7 7 14 14 17 3 1 5 0 7-3l-4-5-3 2c-3-2-6-6-7-9l3-2-4-7z" fill="var(--tile-orange)"/>
      </svg>
      <p class="tile-text">0800 519 306<br>+64 21 948 213</p>
    </div>
    <div class="tile tile-email">
      <svg width="46" height="30" viewBox="0 0 46 30" aria-hidden="true">
        <rect x="1" y="1" width="44" height="28" fill="none" stroke="#fff" stroke-width="2"/>
        <path d="M1 1l22 16L45 1M1 29l16-15M45 29L29 14" fill="none" stroke="#fff" stroke-width="2"/>
      </svg>
      <p class="tile-text">tom@veltra.co</p>
    </div>
    <div class="tile tile-web">
      <svg width="44" height="44" viewBox="0 0 44 44" aria-hidden="true">
        <g fill="none" stroke="#fff" stroke-width="2">
          <circle cx="22" cy="22" r="20"/>
          <ellipse cx="22" cy="22" rx="9" ry="20"/>
          <path d="M22 2v40M2 22h40M5 12h34M5 32h34"/>
        </g>
      </svg>
      <p class="tile-text">www.veltra.co</p>
    </div>
    <div class="panel logo-panel">
      <span class="brand-mark"></span>
      <span class="brand-name">Veltra IT Solutions</span>
    </div>
  </section>
</main>
</body>
</html>
```